high end contractor

high end contracting company we do all phases of construction kitchen,bathrooms,etc... please look at my website before you design www.harborkeybuild.com

would love some sort of lines or logo or both

Industry/Entity Type

Construction

Contact Information for Business Card

company name: oak & meridian contracting address: 318 fenwick st Alderbrook NY 10739 email: harborkeybuild@mailbrook.com website: www.harborkeybuild.com office#: 914-208-3916 fax#: 914-208-5523 dominic valtersen mobile# 917-526-0389

```html
<!DOCTYPE html>
<html lang="en">
<head>
<meta charset="utf-8">
<title>Oak and Meridian Contracting – Business Card</title>
<link rel="stylesheet" href="https://fonts.googleapis.com/css2?family=Open+Sans:wght@400;700&display=swap">
<style>
  :root {
    --card-bg: #414447;
    --accent: #5ec8d8;
    --text: #ffffff;
  }
  html, body {
    margin: 0;
    padding: 0;
    width: 1200px;
    height: 701px;
    overflow: hidden;
    background: var(--card-bg);
  }
  .card {
    position: relative;
    width: 1200px;
    height: 701px;
    background: var(--card-bg);
    font-family: "Open Sans", Arial, sans-serif;
    color: var(--text);
  }
  .company-name {
    position: absolute;
    left: 84px;
    top: 73px;
    margin: 0;
    font-size: 56px;
    font-weight: 700;
    line-height: 70px;
    letter-spacing: 0;
    color: var(--accent);
    text-transform: uppercase;
    white-space: nowrap;
  }
  .contact-list {
    margin: 0;
    padding: 0;
    list-style: none;
  }
  .contact-item {
    position: absolute;
    left: 86px;
    padding-left: 19px;
    font-size: 36px;
    line-height: 44px;
    white-space: nowrap;
  }
  .contact-item::before {
    content: "";
    position: absolute;
    left: 0;
    top: 5px;
    width: 8px;
    height: 33px;
    background: var(--accent);
  }
  .item-website { top: 191px; }
  .item-email   { top: 247px; }
  .item-office  { top: 304px; }
  .item-fax     { top: 360px; }
  .item-person  { top: 416px; display: flex; gap: 36px; }
  .item-address { top: 460px; display: flex; line-height: 58px; }
  .item-address::before { top: 12px; }
  .mobile { position: relative; top: 4px; }
  .address-label { width: 186px; }
  .address-lines { font-style: normal; }
  .address-lines span { display: block; }
</style>
</head>
<body>
  <main class="card">
    <h1 class="company-name">Oak and Meridian Contracting</h1>
    <ul class="contact-list">
      <li class="contact-item item-website">Website: www.harborkeybuild.com</li>
      <li class="contact-item item-email">Email: harborkeybuild@mailbrook.com</li>
      <li class="contact-item item-office">Office: 914 - 208 - 3916</li>
      <li class="contact-item item-fax">Fax: 914 - 208 - 5523</li>
      <li class="contact-item item-person">
        <span class="person-name">Dominic Valtersen</span>
        <span class="mobile">Mobile: 917 - 526 - 0389</span>
      </li>
      <li class="contact-item item-address">
        <span class="address-label">Address:</span>
        <address class="address-lines">
          <span>318 Fenwick Street</span>
          <span>Alderbrook</span>
          <span>NY 10739</span>
        </address>
      </li>
    </ul>
  </main>
</body>
</html>
```